pharmacy/travel clinic business card design

We need a business card for our new business called Brenwick Travel Clinic and Pharmacy. Our primary focus is doing consultations for people before travelling internationally and providing vaccinations and prescriptions for them. While the business is considered a pharmacy, it has more the look and feel of a doctor's office. The design should communicate a professional and trustworthy feel. I have attached a copy of the logo we are going to be using.
Updates
Thanks for the submissions.  If you haven`t been eliminated you are one of the finalists.  Decision will likely be made tomorrow.

Target Market(s)
Customers, other health care professionals, travel agents
Industry/Entity Type
Clinic
Look and feel
Each slider illustrates characteristics of the customer's brand and the style your logo design should communicate.

```html
<!DOCTYPE html>
<html lang="en">
<head>
<meta charset="utf-8">
<title>Brenwick Travel Clinic and Pharmacy – Business Card</title>
<link rel="stylesheet" href="https://fonts.googleapis.com/css2?family=Fira+Sans:wght@400;500;600&display=swap">
<style>
  :root {
    --backdrop: #3b3b3b;
    --blue-deep: #2a48a3;
    --blue-mid: #2a78c8;
    --blue-sky: #29a6e0;
    --green: #8cc63f;
    --white: #ffffff;
    --brand-blue: #2393d9;
  }
  * { margin: 0; padding: 0; box-sizing: border-box; }
  html, body {
    width: 1200px; height: 900px; overflow: hidden;
    background: var(--backdrop);
    font-family: "Fira Sans", Arial, sans-serif;
  }
  .canvas { position: relative; width: 1200px; height: 900px; }
  .card {
    position: absolute; top: 300px; width: 525px; height: 300px;
    border-radius: 22px; overflow: hidden;
  }
  /* Front */
  .card--front {
    left: 58px;
    background: linear-gradient(100deg, var(--blue-deep) 0%, var(--blue-mid) 50%, var(--blue-sky) 100%);
  }
  .front-brand {
    position: absolute; left: 108px; top: 92px;
    display: flex; align-items: flex-start; gap: 14px;
    color: var(--white); font-weight: 600;
  }
  .front-brand .dot {
    width: 34px; height: 34px; border-radius: 50%; background: var(--white); margin-top: 8px;
  }
  .front-brand .name { line-height: 0.95; }
  .front-brand .line-1 { font-size: 50px; display: block; }
  .front-brand .line-2 { font-size: 50px; display: block; }
  .front-brand .line-3 { font-size: 24px; display: block; margin-top: 4px; }

  /* Back */
  .card--back { left: 617px; background: var(--white); }
  .back-top { position: absolute; inset: 0 0 155px 0; background: var(--white); }
  .back-band {
    position: absolute; left: 0; top: 45px; width: 78px; height: 30px; background: var(--blue-sky);
  }
  .back-rule {
    position: absolute; left: 228px; right: 0; top: 126px; height: 14px; background: var(--green);
  }
  .back-brand {
    position: absolute; left: 44px; top: 52px;
    display: flex; align-items: flex-start; gap: 10px;
    color: var(--brand-blue); font-weight: 600;
  }
  .back-brand .dot {
    width: 22px; height: 22px; border-radius: 50%; background: var(--brand-blue); margin-top: 4px;
  }
  .back-brand .name { line-height: 0.98; }
  .back-brand .line-1, .back-brand .line-2 { display: block; font-size: 31px; }
  .back-brand .line-3 { display: block; font-size: 15px; margin-top: 2px; }

  .back-info {
    position: absolute; left: 0; right: 0; bottom: 0; height: 155px;
    background: linear-gradient(100deg, var(--blue-mid) 0%, var(--blue-deep) 100%);
    color: var(--white);
  }
  .person { position: absolute; left: 38px; top: 36px; }
  .person .full-name { font-size: 19px; font-weight: 500; }
  .person .role { font-size: 13px; margin-top: 2px; }
  .address { position: absolute; left: 38px; top: 82px; font-size: 14px; line-height: 21px; }
  .contacts {
    position: absolute; left: 284px; top: 36px; list-style: none;
    font-size: 14px; line-height: 21px;
  }
  .contacts .label { color: var(--green); margin-right: 3px; }
</style>
</head>
<body>
<main class="canvas">
  <section class="card card--front" aria-label="Card front">
    <div class="front-brand">
      <span class="dot"></span>
      <span class="name">
        <span class="line-1">Brenwick</span>
        <span class="line-2">Travel Clinic</span>
        <span class="line-3">and Pharmacy</span>
      </span>
    </div>
  </section>

  <section class="card card--back" aria-label="Card back">
    <div class="back-top">
      <div class="back-band"></div>
      <div class="back-rule"></div>
      <div class="back-brand">
        <span class="dot"></span>
        <span class="name">
          <span class="line-1">Brenwick</span>
          <span class="line-2">Travel Clinic</span>
          <span class="line-3">and Pharmacy</span>
        </span>
      </div>
    </div>
    <div class="back-info">
      <div class="person">
        <p class="full-name">Daniel Whitford</p>
        <p class="role">President/CEO</p>
      </div>
      <p class="address">0000 E. Linden Ave. Ste. 000,<br>Harlow, AZ 123456</p>
      <ul class="contacts">
        <li><span class="label">p:</span>520 555 0000</li>
        <li><span class="label">t:</span>866 555 0000</li>
        <li><span class="label">e:</span>daniel@brenwicktravelclinic.com</li>
        <li><span class="label">w:</span>www.brenwicktravelclinic.com</li>
      </ul>
    </div>
  </section>
</main>
</body>
</html>
```